Gruppo Abitativo Sorena
complete stationary set
Gruppo Abitativo Sorena - Real Estate
Creative Brief
Professional
Marcello Ruffoni
Responsabile di agenzia
Gruppo Abitativo Sorena Via Castellana, 147 20384 Milano - Italy
marcello.ruffoni@gruppoabitativosorena.example
www.gruppoabitativosorena.example
I'm looking for a complete set of stationary: 1. Business Cards 2. Letter Head 3. Presentation Folder 6. Envelopes 7. PowerPoint slide template 9. Note pad cover 10. e-mail signature 11. Fax Cover Please insert QR Code and a photo box in business card. For further information post comments or contact me I will give you all feedback you need
Should have something to that represents our company and will make them want to look at the card again.

```html
<!DOCTYPE html>
<html lang="it">
<head>
<meta charset="utf-8">
<title>Gruppo Abitativo Sorena – Biglietti da visita</title>
<link rel="stylesheet" href="https://fonts.googleapis.com/css2?family=Open+Sans:ital,wght@0,400;0,600;0,800;1,400&display=swap">
<style>
  :root {
    --bg: #e9e6e2;
    --card: #ffffff;
    --navy: #1b2f7a;
    --navy-deep: #0f1d55;
    --band: #d9dbe0;
    --ink: #3b3f47;
    --muted: #8a8f98;
    --photo: #eceef1;
  }
  * { box-sizing: border-box; margin: 0; padding: 0; }
  html, body { width: 1200px; height: 852px; overflow: hidden; }
  body {
    background: var(--bg);
    font-family: "Open Sans", Arial, sans-serif;
    color: var(--ink);
    position: relative;
  }
  .card {
    position: absolute;
    width: 660px;
    height: 370px;
    background: var(--card);
    border-radius: 22px;
    overflow: hidden;
    box-shadow: 0 6px 18px rgba(0,0,0,.18);
  }
  .card--front { left: 60px; top: 40px; }
  .card--back { left: 480px; top: 442px; }
  .card__edge { position: absolute; inset: 0; width: 100%; height: 100%; }

  .brand { position: absolute; display: flex; flex-direction: column; }
  .brand__row { display: flex; align-items: center; gap: 10px; }
  .brand__mark { width: 20px; height: 20px; background: var(--navy); }
  .brand__name {
    font-weight: 800; font-size: 26px; color: var(--navy);
    letter-spacing: .4px; text-transform: uppercase; line-height: 1; white-space: nowrap;
  }
  .brand__url {
    font-size: 10px; color: var(--muted); letter-spacing: 2.6px;
    margin-top: 6px; margin-left: 30px; white-space: nowrap;
  }
  .card--front .brand { left: 60px; top: 46px; }
  .card--back .brand { left: 120px; top: 48px; }

  .address { position: absolute; font-size: 14px; line-height: 1.4; color: var(--ink); }
  .card--front .address { left: 120px; top: 128px; }
  .card--back .address { left: 100px; top: 222px; width: 200px; text-align: right; }

  .photo-box {
    position: absolute; left: 480px; top: 46px; width: 130px; height: 150px;
    background: var(--photo); border: 1px solid #dfe2e6;
  }
  .person { position: absolute; text-align: right; }
  .person__name { font-weight: 800; font-size: 17px; color: var(--navy); }
  .person__role { font-style: italic; font-size: 12px; color: var(--muted); }
  .card--front .person { right: 50px; top: 210px; }
  .card--back .person { left: 100px; top: 160px; width: 200px; }

  .contacts { position: absolute; list-style: none; font-size: 12.5px; }
  .contacts li { display: flex; align-items: center; gap: 8px; height: 21px; white-space: nowrap; }
  .contacts svg { width: 13px; height: 13px; fill: var(--navy); flex: none; }
  .card--front .contacts { left: 110px; top: 244px; }
  .card--back .contacts { left: 318px; top: 150px; }
</style>
</head>
<body>

<section class="card card--front">
  <svg class="card__edge" viewBox="0 0 660 370" preserveAspectRatio="none" aria-hidden="true">
    <defs>
      <linearGradient id="swoosh-a" x1="0" y1="0" x2="1" y2="1">
        <stop offset="0" stop-color="#2a44a3"/>
        <stop offset="1" stop-color="#0f1d55"/>
      </linearGradient>
    </defs>
    <path d="M0,40 C55,150 60,280 120,370 L96,370 C48,280 40,165 0,75 Z" fill="var(--band)"/>
    <path d="M0,75 C40,165 48,280 96,370 L0,370 Z" fill="url(#swoosh-a)"/>
  </svg>

  <div class="brand">
    <div class="brand__row"><span class="brand__mark"></span><span class="brand__name">Gruppo Abitativo Sorena</span></div>
    <span class="brand__url">www.gruppoabitativosorena.example</span>
  </div>

  <p class="address">Gruppo Abitativo Sorena<br>Via Castellana, 147<br>20384 Milano - Italy</p>

  <div class="photo-box" role="img" aria-label="Spazio per la foto del responsabile"></div>

  <div class="person">
    <p class="person__name">Marcello Ruffoni</p>
    <p class="person__role">Responsabile di agenzia</p>
  </div>

  <ul class="contacts">
    <li><svg viewBox="0 0 16 16"><path d="M3 1h3l1 4-2 1a9 9 0 0 0 5 5l1-2 4 1v3c0 1-1 2-2 2A13 13 0 0 1 1 3c0-1 1-2 2-2z"/></svg>+39 02 48 61 730</li>
    <li><svg viewBox="0 0 16 16"><path d="M4 0h8a1 1 0 0 1 1 1v14a1 1 0 0 1-1 1H4a1 1 0 0 1-1-1V1a1 1 0 0 1 1-1zm1 2v10h6V2zm3 11a1 1 0 1 0 0 2 1 1 0 0 0 0-2z"/></svg>+39 347 58 21 904</li>
    <li><svg viewBox="0 0 16 16"><path d="M1 4h14v9H1zm2 2v5h10V6zM4 1h8v2H4z"/></svg>+39 02 48 61 731</li>
    <li><svg viewBox="0 0 16 16"><path d="M8 0a8 8 0 1 0 4 15l-1-2a6 6 0 1 1 3-5v1a1 1 0 0 1-2 0V8a4 4 0 1 0-1 3 3 3 0 0 0 5-2V8a8 8 0 0 0-8-8zm0 6a2 2 0 1 1 0 4 2 2 0 0 1 0-4z"/></svg>marcello.ruffoni@gruppoabitativosorena.example</li>
  </ul>
</section>

<section class="card card--back">
  <svg class="card__edge" viewBox="0 0 660 370" preserveAspectRatio="none" aria-hidden="true">
    <defs>
      <linearGradient id="swoosh-b" x1="0" y1="0" x2="1" y2="1">
        <stop offset="0" stop-color="#2a44a3"/>
        <stop offset="1" stop-color="#0f1d55"/>
      </linearGradient>
    </defs>
    <path d="M0,30 C70,120 80,270 120,370 L92,370 C55,275 45,150 0,70 Z" fill="var(--band)"/>
    <path d="M0,70 C45,150 55,275 92,370 L0,370 Z" fill="url(#swoosh-b)"/>
  </svg>

  <div class="brand">
    <div class="brand__row"><span class="brand__mark"></span><span class="brand__name">Gruppo Abitativo Sorena</span></div>
    <span class="brand__url">www.gruppoabitativosorena.example</span>
  </div>

  <div class="person">
    <p class="person__name">Marcello Ruffoni</p>
    <p class="person__role">Responsabile di agenzia</p>
  </div>

  <p class="address">Gruppo Abitativo Sorena<br>Via Castellana, 147<br>20384 Milano - Italy</p>

  <ul class="contacts">
    <li><svg viewBox="0 0 16 16"><path d="M3 1h3l1 4-2 1a9 9 0 0 0 5 5l1-2 4 1v3c0 1-1 2-2 2A13 13 0 0 1 1 3c0-1 1-2 2-2z"/></svg>+39 02 48 61 730</li>
    <li><svg viewBox="0 0 16 16"><path d="M4 0h8a1 1 0 0 1 1 1v14a1 1 0 0 1-1 1H4a1 1 0 0 1-1-1V1a1 1 0 0 1 1-1zm1 2v10h6V2zm3 11a1 1 0 1 0 0 2 1 1 0 0 0 0-2z"/></svg>+39 347 58 21 904</li>
    <li><svg viewBox="0 0 16 16"><path d="M1 4h14v9H1zm2 2v5h10V6zM4 1h8v2H4z"/></svg>+39 02 48 61 731</li>
    <li><svg viewBox="0 0 16 16"><path d="M8 0a8 8 0 1 0 4 15l-1-2a6 6 0 1 1 3-5v1a1 1 0 0 1-2 0V8a4 4 0 1 0-1 3 3 3 0 0 0 5-2V8a8 8 0 0 0-8-8zm0 6a2 2 0 1 1 0 4 2 2 0 0 1 0-4z"/></svg>marcello.ruffoni@gruppoabitativosorena.example</li>
    <li><svg viewBox="0 0 16 16"><path d="M8 0a8 8 0 1 1 0 16A8 8 0 0 1 8 0zm0 1.5C7 1.5 6 4 6 7h4c0-3-1-5.5-2-5.5zM2 7h3c0-2 .4-3.8 1-5A6.5 6.5 0 0 0 2 7zm9 0h3a6.5 6.5 0 0 0-4-5c.6 1.2 1 3 1 5zM2 9a6.5 6.5 0 0 0 4 5c-.6-1.2-1-3-1-5zm4 0c0 3 1 5.5 2 5.5s2-2.5 2-5.5zm5 0c0 2-.4 3.8-1 5a6.5 6.5 0 0 0 4-5z"/></svg>www.gruppoabitativosorena.example</li>
  </ul>
</section>

</body>
</html>
```